Lernpfad-Muster für Großhändler (interne Verwendung)
Zielgruppe
Die KORVA Großmarkt Deutschland GmbH ist als Teil der KORVA Gruppe Großhändler und richtet sich mit seinem Sortiment an Gewerbetreibende. Um 'Profi für Profi' zu sein (und zu bleiben), ist konstante Weiterbildung wichtig. Dafür haben die Mitarbeiter - je nach Position - einen umfangreichen Lernpfad, der aus Trainings und Online-Modulen (eLearnings, Webinare...) besteht und aus dem sie frei ihre Weiterbildungsangebote wählen können.
Diese Lernpfade sollen bekannter werden, v.a. neue Kollegen sollen schon am ersten Tag wissen, was sie tun können, um ihren neuen Arbeitgeber, die Kundengruppen, die Produkte, die Strategie etc. kennenzulernen. Azubis sollen hier eine Art 'Lehrplan' vorfinden. Abnehmer sollen auch alle langjährigen Mitarbeiter und auch deren Führungskräfte sein, um Weiterbildung zu besprechen und gezielt zu planen.
Wir wünschen uns von Ihnen ein Muster, das wir nutzen können, um die Lernpfade entsprechend den Positionen auszugestalten. Beispiel: Wir würden gerne Ihr Muster nehmen und daraus ein Angebot für Kassierer und für Menschen am Wareneingang stricken (unterschiedliche Vorschläge für Trainings und eLearnings).
Die Lernpfade werden übers Intranet zur Verfügung gestellt, den Vertragsunterlagen beigelegt (geplant) und über E-Mailverteiler an Schlüsselpersonen weitergegeben.
Das Thema ist eine Fortsetzung der Training-Kampagne (Poster hängt neben weiteren Dokumenten an).
Aufgabenstellung
Die Flyer werden ausschließlich intern verwendet.
Variante: sechsseitiger Wickelpfalz oder in der Mitte geknickt (also vier Seiten)
Größe: A4
Gesetzte Seiten:
Titelseite:
Bitte den Schraubolf verwenden, das Korva-Logo, das HR-Logo, einen beispielhaften Lernpfad-Titel (z.B. "Mitarbeiter Verkauf" oder "Abteilungsleiter Warenannahme")
Seite Trainings:
Auf einen Blick soll hier ersichtlich sein, dass es sich um Trainings handelt. Großes Piktogramm, Schraffur - wie auch immer.
Piktogramme oder kleine Bildchen (existieren noch nicht; z.B. für Rhetorik, Veränderung, Konflikt, Führung) mit Trainingstitel (z.B. "Führung konkret") und Dauer (1 Tag z.B.). 30 dieser Bildchen müssen auf eine Seite passen.
Farbliche Kennzeichnung: Führung (violett), Produkte (gelb), Systeme (grün), Soft Skills (blau); zur Einarbeitung empfohlene Trainings werden zusätzlich mit einem Sternchen, verpflichtende Trainings zusätzlich mit einem Ausrufezeichen versehen.
Seite Online-Trainings:
Auf einen Blick soll hier ersichtlich sein, dass es sich um Online-Trainings handelt. Großes Piktogramm, Schraffur - wie auch immer.
Piktogramme oder kleine Bildchen (liegen vor; z.B. für LMIV, Hygiene, Arbeitsrecht, Unsere Kunden) mit Trainingstitel und Dauer (30 Minuten z.B.). 30 dieser Bildchen müssen auf eine Seite passen.
Farbliche Kennzeichnung: wie oben

```html
<!DOCTYPE html>
<html lang="de">
<head>
<meta charset="utf-8">
<title>Lernpfad – Kontakte und Trainer</title>
<link rel="stylesheet" href="https://fonts.googleapis.com/css2?family=Open+Sans:wght@400;700&display=swap">
<style>
  :root {
    --page-bg: #f1f1f1;
    --text: #454545;
    --heading: #3a3a3a;
    --photo-light: #e4eef0;
    --photo-mid: #b9cbd2;
    --photo-dark: #4a5a6c;
  }
  * { box-sizing: border-box; margin: 0; padding: 0; }
  html, body { width: 846px; height: 1200px; overflow: hidden; }
  body {
    background: var(--page-bg);
    color: var(--text);
    font-family: "Open Sans", Arial, sans-serif;
    position: relative;
  }
  .info {
    position: absolute;
    top: 100px;
    width: 360px;
  }
  .info--portal { left: 45px; }
  .info--mail { left: 432px; }
  .info__title {
    font-size: 16px;
    font-weight: 700;
    color: var(--heading);
    margin-bottom: 20px;
  }
  .info__value {
    font-size: 15.5px;
    line-height: 1.3;
  }
  .trainers {
    position: absolute;
    top: 267px;
    left: 45px;
    display: grid;
    grid-template-columns: 387px 387px;
    row-gap: 20px;
  }
  .trainer {
    display: flex;
    height: 121px;
  }
  .trainer__photo {
    width: 174px;
    height: 121px;
    flex: none;
  }
  .trainer__photo--office {
    background: linear-gradient(90deg, var(--photo-light) 0%, var(--photo-mid) 55%, var(--photo-dark) 100%);
  }
  .trainer__photo--team {
    background: linear-gradient(90deg, var(--photo-mid) 0%, var(--photo-dark) 45%, var(--photo-light) 100%);
  }
  .trainer__photo--bright {
    background: linear-gradient(90deg, #ffffff 0%, #f3f5f6 50%, #c9b6ad 100%);
  }
  .trainer__text {
    padding-left: 17px;
    padding-top: 0;
  }
  .trainer__name {
    font-size: 16px;
    font-weight: 700;
    color: var(--heading);
    margin-bottom: 20px;
    line-height: 1.2;
  }
  .trainer__topic {
    font-size: 15.5px;
    line-height: 1.25;
    max-width: 190px;
  }
  .company {
    position: absolute;
    top: 1048px;
    left: 432px;
    font-size: 15.5px;
    line-height: 1.3;
  }
</style>
</head>
<body>
  <section class="info info--portal">
    <h2 class="info__title">Weg ins Trainingsportal:</h2>
    <p class="info__value">http://lernportal.korvagruppe-netzwerk.<br>com/irj/portal/learn</p>
  </section>
  <section class="info info--mail">
    <h2 class="info__title">E-Mailadresse für Rückfragen:</h2>
    <p class="info__value">trainingkgd@korva-gm.de</p>
  </section>

  <main class="trainers">
    <article class="trainer">
      <div class="trainer__photo trainer__photo--office" role="img" aria-label="Porträtfoto der Trainerin im Büro"></div>
      <div class="trainer__text">
        <h3 class="trainer__name">Carola Wendt</h3>
        <p class="trainer__topic">Konfliktmanagment für Führungspersonal</p>
      </div>
    </article>
    <article class="trainer">
      <div class="trainer__photo trainer__photo--team" role="img" aria-label="Foto des Trainers vor seinem Team"></div>
      <div class="trainer__text">
        <h3 class="trainer__name">Jonas Ebert</h3>
        <p class="trainer__topic">Gleichberechtigung am Arbeitsplatz</p>
      </div>
    </article>
    <article class="trainer">
      <div class="trainer__photo trainer__photo--office" role="img" aria-label="Porträtfoto des Trainers im Büro"></div>
      <div class="trainer__text">
        <h3 class="trainer__name">Dieter Kramm</h3>
        <p class="trainer__topic">Kaufmännischer Vertrieb</p>
      </div>
    </article>
    <article class="trainer">
      <div class="trainer__photo trainer__photo--bright" role="img" aria-label="Porträtfoto der Trainerin vor hellem Hintergrund"></div>
      <div class="trainer__text">
        <h3 class="trainer__name">Nadine Lorenz</h3>
        <p class="trainer__topic">Lagerservice für Lebensmittel</p>
      </div>
    </article>
    <article class="trainer">
      <div class="trainer__photo trainer__photo--office" role="img" aria-label="Porträtfoto der Trainerin im Büro"></div>
      <div class="trainer__text">
        <h3 class="trainer__name">Carola Wendt</h3>
        <p class="trainer__topic">Konfliktmanagment für Führungspersonal</p>
      </div>
    </article>
    <article class="trainer">
      <div class="trainer__photo trainer__photo--team" role="img" aria-label="Foto des Trainers vor seinem Team"></div>
      <div class="trainer__text">
        <h3 class="trainer__name">Jonas Ebert</h3>
        <p class="trainer__topic">Gleichberechtigung am Arbeitsplatz</p>
      </div>
    </article>
    <article class="trainer">
      <div class="trainer__photo trainer__photo--office" role="img" aria-label="Porträtfoto des Trainers im Büro"></div>
      <div class="trainer__text">
        <h3 class="trainer__name">Dieter Kramm</h3>
        <p class="trainer__topic">Kaufmännischer Vertrieb</p>
      </div>
    </article>
    <article class="trainer">
      <div class="trainer__photo trainer__photo--bright" role="img" aria-label="Porträtfoto der Trainerin vor hellem Hintergrund"></div>
      <div class="trainer__text">
        <h3 class="trainer__name">Nadine Lorenz</h3>
        <p class="trainer__topic">Lagerservice für Lebensmittel</p>
      </div>
    </article>
  </main>

  <address class="company" style="font-style: normal;">
    KORVA Großmarkt Deutschland GmbH<br>
    Hafenstr. 7<br>
    40221 Düsseldorf
  </address>
</body>
</html>
```